Square graphic for social media post

I want to create a 1080 x 1080px all-black image for the quote below that I can share on social media. I want the emphasis to be primarily on the quote, secondarily on the portrait, and third (smallest) on the logo. I want the background on the portrait to be edited so it's transparent and just shows the face of the person on a black background (no brick wall visible).

Graphic color: black
Text color: white
Content: "What we went through is going to make the greatest generation of hoteliers our industry has ever seen." << biggest text
Dorian Welk << smaller text
President, Marrowgate Hotels << smaller text
[image of person - use whichever version looks better to you]
[Add Lodging Ledger logo - whichever looks better to you]

This image needs to be readable when sized down much smaller (400x400?) so want the text and portrait to take up most of the space.

I'd like the output both as PNG and original file (preferably Canva). Thanks!

Target Market(s)

Hotel managers

Industry/Entity Type

Hospitality

Font styles to use
Sans Serif

Colors

Designer to choose colors to be used in the design.

Requirements
Must have
• Needs to focus on the quote and the person quoted (the portrait)

```html
<!DOCTYPE html>
<html lang="en">
<head>
<meta charset="utf-8">
<title>Lodging Ledger – Quote Card</title>
<link href="https://fonts.googleapis.com/css2?family=Roboto+Condensed:wght@400;500;700&display=swap" rel="stylesheet">
<style>
  :root {
    --bg: #000000;
    --ink: #ffffff;
    --ink-soft: #d9d9d9;
    --portrait-light: #8a8a8a;
    --portrait-mid: #3c3c3c;
    --portrait-dark: #0a0a0a;
  }
  html, body {
    margin: 0;
    padding: 0;
    width: 1200px;
    height: 1200px;
    overflow: hidden;
    background: var(--bg);
  }
  .card {
    position: relative;
    width: 1200px;
    height: 1200px;
    background: var(--bg);
    overflow: hidden;
    font-family: "Roboto Condensed", "Arial Narrow", sans-serif;
    color: var(--ink);
  }
  .portrait {
    position: absolute;
    left: 0;
    top: 70px;
    width: 760px;
    height: 1130px;
    background:
      radial-gradient(ellipse 38% 42% at 48% 46%, var(--portrait-light) 0%, var(--portrait-mid) 60%, transparent 100%),
      radial-gradient(ellipse 70% 30% at 50% 100%, #2a2a2a 0%, transparent 100%),
      var(--portrait-dark);
    border-radius: 48% 48% 0 0 / 30% 30% 0 0;
  }
  .brand {
    position: absolute;
    left: 800px;
    top: 62px;
    width: 250px;
    text-align: center;
    font-weight: 500;
    font-size: 22px;
    letter-spacing: 5px;
    text-transform: uppercase;
    color: var(--ink);
  }
  .brand-dot {
    display: block;
    width: 8px;
    height: 8px;
    margin: 0 auto 10px;
    border-radius: 50%;
    background: var(--ink);
  }
  .quote {
    position: absolute;
    left: 0;
    top: 0;
    margin: 0;
    font-weight: 700;
    font-size: 78px;
    line-height: 80px;
    letter-spacing: -0.5px;
    color: var(--ink);
  }
  .quote-line {
    position: absolute;
    white-space: nowrap;
  }
  .attribution {
    position: absolute;
    left: 790px;
    top: 960px;
    margin: 0;
    white-space: nowrap;
  }
  .attribution-name {
    display: block;
    font-weight: 700;
    font-size: 40px;
    line-height: 46px;
    color: var(--ink);
  }
  .attribution-role {
    display: block;
    margin-top: 4px;
    font-weight: 400;
    font-size: 28px;
    line-height: 34px;
    color: var(--ink-soft);
  }
</style>
</head>
<body>
  <main class="card">
    <div class="portrait" role="img" aria-label="Black and white head-and-shoulders portrait of Dorian Welk, smiling, in a dark jacket and white shirt, on black"></div>

    <div class="brand"><span class="brand-dot"></span>Lodging Ledger</div>

    <blockquote class="quote" aria-label="What we went through is going to make the greatest generation of hoteliers our industry has ever seen">
      <span class="quote-line" style="left:722px; top:197px;">What we</span>
      <span class="quote-line" style="left:747px; top:275px;">went through</span>
      <span class="quote-line" style="left:752px; top:355px;">is going to</span>
      <span class="quote-line" style="left:769px; top:436px;">make the</span>
      <span class="quote-line" style="left:791px; top:522px;">greatest</span>
      <span class="quote-line" style="left:774px; top:602px;">generation</span>
      <span class="quote-line" style="left:758px; top:680px;">of hoteliers</span>
      <span class="quote-line" style="left:714px; top:758px;">our industry</span>
      <span class="quote-line" style="left:697px; top:842px;">has ever seen</span>
    </blockquote>

    <p class="attribution">
      <span class="attribution-name">Dorian Welk</span>
      <span class="attribution-role">President, Marrowgate Hotels</span>
    </p>
  </main>
</body>
</html>
```